Tervo's Glen

I need a Bussiness Card for my new company in Miami Beach, my company is based in Winwood Miami and all around me is arts soo I would like my card with stripes, art design.

Artists, Actress, actors, show bussiness

It Company

• Art Design

```html
<!DOCTYPE html>
<html lang="en">
<head>
<meta charset="utf-8">
<title>Tervo's Glen — Business Card</title>
<link rel="stylesheet" href="https://fonts.googleapis.com/css2?family=Poiret+One&family=Questrial&display=swap">
<style>
  :root {
    --page: #ededed;
    --card: #0b0b0b;
    --stripe-red: #d62b35;
    --stripe-gold: #f4a21f;
    --brand-red: #d8262f;
    --name-gold: #f2b021;
    --title-brown: #8f5a26;
    --contact-gold: #d7a047;
    --partner-blue: #1d7fd0;
  }
  * { box-sizing: border-box; margin: 0; padding: 0; }
  html, body {
    width: 1200px; height: 800px; overflow: hidden;
    background: var(--page);
  }
  .canvas {
    position: relative; width: 1200px; height: 800px;
    display: flex; align-items: center; justify-content: center; gap: 60px;
  }
  .card {
    position: relative; width: 520px; height: 297px;
    background: var(--card); overflow: hidden;
    box-shadow: 0 2px 6px rgba(0,0,0,0.18);
  }
  .stripe-band { position: absolute; top: 0; height: 100%; }
  .stripe-band--left { left: 0; width: 100px; }
  .stripe-band--right { right: 0; width: 120px; }
  .stripe-red { fill: var(--stripe-red); }
  .stripe-gold { fill: var(--stripe-gold); }

  /* Front */
  .brand {
    position: absolute; left: 150px; top: 72px;
    display: flex; align-items: center; gap: 12px;
  }
  .brand__mark { width: 18px; height: 18px; background: var(--stripe-gold); }
  .brand__name {
    font-family: "Questrial", sans-serif; font-size: 38px;
    color: var(--brand-red); line-height: 1; white-space: nowrap;
  }
  .person { position: absolute; left: 150px; top: 176px; }
  .person__name {
    font-family: "Poiret One", sans-serif; font-size: 24px; font-weight: 400;
    color: var(--name-gold); letter-spacing: 1px; text-transform: uppercase;
    -webkit-text-stroke: 0.6px var(--name-gold);
  }
  .person__title {
    font-family: "Questrial", sans-serif; font-size: 11px;
    color: var(--title-brown); margin-top: 2px;
  }

  /* Back */
  .contact {
    position: absolute; left: 118px; top: 60px;
    font-family: "Questrial", sans-serif; font-size: 14px; line-height: 1.65;
    color: var(--contact-gold); list-style: none;
  }
  .partner {
    position: absolute; left: 118px; top: 232px;
    display: flex; align-items: center; gap: 8px;
  }
  .partner__mark { width: 14px; height: 14px; border-radius: 50%; background: var(--partner-blue); }
  .partner__name {
    font-family: "Questrial", sans-serif; font-size: 16px; color: var(--partner-blue);
  }
</style>
</head>
<body>
<main class="canvas">

  <!-- Back side -->
  <section class="card card--back" aria-label="Business card, back">
    <svg class="stripe-band stripe-band--left" viewBox="0 0 100 297" preserveAspectRatio="none" aria-hidden="true">
      <rect class="stripe-red" x="4" y="0" width="5" height="297"/>
      <rect class="stripe-gold" x="13" y="0" width="7" height="297"/>
      <rect class="stripe-red" x="24" y="0" width="3" height="297"/>
      <rect class="stripe-gold" x="31" y="0" width="4" height="297"/>
      <rect class="stripe-red" x="40" y="0" width="8" height="297"/>
      <rect class="stripe-gold" x="52" y="0" width="3" height="297"/>
      <rect class="stripe-red" x="59" y="0" width="4" height="297"/>
      <rect class="stripe-gold" x="67" y="0" width="6" height="297"/>
      <rect class="stripe-red" x="78" y="0" width="3" height="297"/>
    </svg>
    <ul class="contact">
      <li>tervomaldane@tervosglen.net</li>
      <li>Cel. 786-555-0142</li>
      <li>418 Nw 31st St Miami Florida 33100</li>
      <li>@tervosglen Photos-Posts</li>
      <li>www.tervosglen.net</li>
    </ul>
    <div class="partner">
      <span class="partner__mark" aria-hidden="true"></span>
      <span class="partner__name">Foundry Set</span>
    </div>
    <svg class="stripe-band stripe-band--right" viewBox="0 0 120 297" preserveAspectRatio="none" aria-hidden="true">
      <rect class="stripe-red" x="10" y="0" width="4" height="297"/>
      <rect class="stripe-gold" x="19" y="0" width="6" height="297"/>
      <rect class="stripe-red" x="30" y="0" width="3" height="297"/>
      <rect class="stripe-gold" x="38" y="0" width="7" height="297"/>
      <rect class="stripe-red" x="50" y="0" width="5" height="297"/>
      <rect class="stripe-gold" x="60" y="0" width="4" height="297"/>
      <rect class="stripe-red" x="69" y="0" width="7" height="297"/>
      <rect class="stripe-gold" x="81" y="0" width="5" height="297"/>
      <rect class="stripe-red" x="91" y="0" width="3" height="297"/>
      <rect class="stripe-gold" x="99" y="0" width="6" height="297"/>
      <rect class="stripe-red" x="110" y="0" width="4" height="297"/>
    </svg>
  </section>

  <!-- Front side -->
  <section class="card card--front" aria-label="Business card, front">
    <svg class="stripe-band stripe-band--left" viewBox="0 0 100 297" preserveAspectRatio="none" aria-hidden="true">
      <rect class="stripe-red" x="4" y="0" width="5" height="297"/>
      <rect class="stripe-gold" x="13" y="0" width="7" height="297"/>
      <rect class="stripe-red" x="24" y="0" width="3" height="297"/>
      <rect class="stripe-gold" x="31" y="0" width="4" height="297"/>
      <rect class="stripe-red" x="40" y="0" width="8" height="297"/>
      <rect class="stripe-gold" x="52" y="0" width="3" height="297"/>
      <rect class="stripe-red" x="59" y="0" width="4" height="297"/>
      <rect class="stripe-gold" x="67" y="0" width="6" height="297"/>
      <rect class="stripe-red" x="78" y="0" width="3" height="297"/>
    </svg>
    <div class="brand">
      <span class="brand__mark" aria-hidden="true"></span>
      <span class="brand__name">Tervo's Glen</span>
    </div>
    <div class="person">
      <h1 class="person__name">Tervo Maldane</h1>
      <p class="person__title">TV Producer, Talent Hunt</p>
    </div>
    <svg class="stripe-band stripe-band--right" viewBox="0 0 120 297" preserveAspectRatio="none" aria-hidden="true">
      <rect class="stripe-red" x="10" y="0" width="4" height="297"/>
      <rect class="stripe-gold" x="19" y="0" width="6" height="297"/>
      <rect class="stripe-red" x="30" y="0" width="3" height="297"/>
      <rect class="stripe-gold" x="38" y="0" width="7" height="297"/>
      <rect class="stripe-red" x="50" y="0" width="5" height="297"/>
      <rect class="stripe-gold" x="60" y="0" width="4" height="297"/>
      <rect class="stripe-red" x="69" y="0" width="7" height="297"/>
      <rect class="stripe-gold" x="81" y="0" width="5" height="297"/>
      <rect class="stripe-red" x="91" y="0" width="3" height="297"/>
      <rect class="stripe-gold" x="99" y="0" width="6" height="297"/>
      <rect class="stripe-red" x="110" y="0" width="4" height="297"/>
    </svg>
  </section>

</main>
</body>
</html>
```